IT Consulting Site Revamping for Marlune

I've put a skeleton together on my website, but realize I need some help (it's http://pilot.marlune-example.ca).
I've pulled together tidbits from other websites, but really need my site to be cleaned up, and really spruced up.
I primarily focus on the IT needs of small to medium size businesses, taking care of everything from their servers and networks down to their workstations.
I also want a page listing the vendors (and logos) that I work with including Quillsoft, Zentrix, Halvor, Brax, TL, RZO, VELK, Trevo, Gatemoor.
There should also be a simple form to get a quote that will email me.
The final design should communicate strength and reliability.
I would like this to be a fully functional website, that I can upload to Plumly Pages, with the same sort of pages that are existing on http://pilot.marlune-example.ca
Updates
Hey everyone,
Hi everyone,
Reason: Hi all,
There are some designers that would like to submit some new designs, so I'm extending the deadline.
Thanks,
Target Market(s)
Small to medium size business owners. This will primarily be males who work in the oil and gas industry.
Industry/Entity Type
Consulting
Look and feel
Each slider illustrates characteristics of the customer's brand and the style your logo design should communicate.

```html
<!DOCTYPE html>
<html lang="en">
<head>
<meta charset="utf-8">
<title>Marlune Solutions</title>
<link rel="stylesheet" href="https://fonts.googleapis.com/css2?family=Archivo+Black&family=Arimo:wght@400;700&family=Noto+Sans:wght@400;700&display=swap">
<style>
:root{
  --brand:#1f7fc0;
  --brand-dark:#0a5c98;
  --nav:#0b7dc4;
  --band:#2a6fae;
  --footer:#2a77b0;
  --ink:#1a1a1a;
  --muted:#555;
  --page:#efefef;
  --card:#f7f7f7;
  --line:#cfcfcf;
  --accent:#c41a1a;
}
*{margin:0;padding:0;box-sizing:border-box}
html,body{width:1200px;height:1034px;overflow:hidden}
body{position:relative;background:var(--page);font-family:"Noto Sans",sans-serif;color:var(--ink)}
.abs{position:absolute}

.header{left:0;top:0;width:1200px;height:123px;border-top:3px solid #111;background:linear-gradient(#e4eef7,#fff 70%)}
.brand-mark{left:180px;top:14px;width:96px;height:96px;border-radius:50%;background:var(--brand)}
.brand-name{left:300px;top:26px;font:700 56px/1 "Arimo",sans-serif;color:var(--brand);letter-spacing:-1px}
.brand-sub{left:304px;top:86px;font:400 15px/1 "Arimo",sans-serif;color:var(--brand);letter-spacing:10px}
.social{top:24px;display:flex;align-items:center;gap:6px;font:700 13px "Arimo",sans-serif;color:var(--brand)}
.social i{width:14px;height:14px;background:var(--brand);display:block}

.nav{left:0;top:123px;width:1200px;height:35px;background:var(--nav);border-bottom:1px solid #5aa9dc}
.nav ul{position:absolute;left:178px;top:0;display:flex;list-style:none;height:35px}
.nav li{font:400 13px/35px "Arimo",sans-serif;color:#fff;padding:0 20px;border-right:1px solid #3d9ad4}
.nav li.active{background:var(--brand-dark)}

.hero-bg{left:0;top:158px;width:1200px;height:251px;background:#1d4f8a}
.hero{left:179px;top:159px;width:842px;height:249px;border:2px solid #2ec3f2;
  background:linear-gradient(90deg,#02081c 0%,#0c2a5e 35%,#5a6f95 65%,#b9c3d6 100%)}
.hero-line{font:400 27px/1 "Archivo Black",sans-serif;color:#fff;letter-spacing:1px}
.hero-line.red{color:var(--accent);text-shadow:0 0 2px #fff}
.band{left:0;top:409px;width:1200px;height:5px;background:var(--band)}

.content{left:178px;top:414px;width:844px;height:486px;background:linear-gradient(#e3f2fb,#fff 60px)}
.welcome{left:196px;top:428px;font:700 27px/1 "Noto Sans",sans-serif;color:var(--band)}
.intro{left:196px;top:456px;width:808px;font-size:11.5px;line-height:14.2px;text-align:justify;letter-spacing:.2px}
.intro p{margin-bottom:14px}
.learn{left:932px;top:575px;font:700 9.5px "Noto Sans",sans-serif;color:var(--accent);display:flex;align-items:center;gap:4px}
.learn svg{display:block}

.section-title{font:400 16px/1 "Noto Sans",sans-serif;color:#444}
.section-icon{width:22px;height:30px;border-radius:4px;background:linear-gradient(#f3a060,#d84a2a)}

.card{top:634px;width:158px;height:136px;background:linear-gradient(#fff,var(--card));border:1px solid var(--line);box-shadow:0 4px 5px -3px #aaa}
.card .thumb{position:absolute;left:8px;top:7px;width:57px;height:56px;border:1px solid #9ab;background:linear-gradient(135deg,#d9dee4,#8797a8)}
.card h3{position:absolute;left:72px;top:14px;width:82px;font:700 10px/13px "Noto Sans",sans-serif}
.card p{position:absolute;left:7px;top:70px;width:144px;font-size:9px;line-height:10px;color:#222}
.card .more{position:absolute;right:14px;bottom:10px}

.partners{left:196px;top:816px;width:808px;height:69px;border:1px solid #bbb;border-radius:4px;background:#fff;box-shadow:0 6px 6px -4px #aaa}
.partners ul{list-style:none;display:flex;justify-content:space-between;align-items:center;height:100%;padding:0 12px}
.partners li{font:700 17px "Arimo",sans-serif;color:#1b3f7a}

.footer{left:0;top:900px;width:1200px;height:134px;background:var(--footer);border-bottom:5px solid #1a5c90}
.footer-links{left:0;top:912px;width:1200px;text-align:center;font-size:10.5px;color:#fff;letter-spacing:.3px}
.footer-links span{margin:0 7px}
.copyright{left:0;top:1005px;width:1200px;text-align:center;font-size:8.5px;color:#fff}
.footer-rule{left:0;top:1020px;width:1200px;height:1px;background:#7fb2d8}
</style>
</head>
<body>
<header class="abs header"></header>
<div class="abs brand-mark"></div>
<div class="abs brand-name">Marlune</div>
<div class="abs brand-sub">solutions</div>
<a class="abs social" style="left:892px"><i></i>Folio</a>
<a class="abs social" style="left:955px"><i></i>Chirpline</a>

<nav class="abs nav"><ul>
  <li class="active">HOME</li><li style="padding:0 24px">OUR SERVICES</li><li style="padding:0 22px">ABOUT US</li><li style="border:0;padding:0 22px">CONTACT US</li>
</ul></nav>

<div class="abs hero-bg"></div>
<div class="abs hero" role="img" aria-label="Technician drawing a network diagram of servers, routers and client PCs on a glass board"></div>
<div class="abs hero-line" style="left:195px;top:219px">Small Business</div>
<div class="abs hero-line" style="left:240px;top:256px">Information Technology</div>
<div class="abs hero-line" style="left:284px;top:293px">Services Easy</div>
<div class="abs hero-line red" style="left:199px;top:335px">Affordable and Reliable</div>
<div class="abs band"></div>

<main class="abs content"></main>
<h1 class="abs welcome">Welcome to Marlune Solutions</h1>
<div class="abs intro">
  <p>Marlune Solutions is a computer solutions provider and IT consulting firm that supports a wide variety of local small businesses in the Calgary area primarily. Our company also provides IT services to businesses throughout Alberta on special projects.</p>
  <p>Marlune has been trusted for over the last 7 years by small business companies like yours. Whether you are looking for an ongoing computer support company, looking to outsource your small business computer work, or just looking for a computer company to help you solve a computer problem, Marlune is your right choice.</p>
  <p>We have a diversity of small business support solutions. We provide in office, over the phone, remote or drop-off computer technical support services to small business.</p>
</div>
<div class="abs learn">Learn more
  <svg width="13" height="13" viewBox="0 0 13 13"><circle cx="6.5" cy="6.5" r="5.5" fill="#f2f2f2" stroke="#999"/><path d="M5 4l3 2.5L5 9z" fill="#777"/></svg>
</div>

<div class="abs section-icon" style="left:198px;top:602px" role="img" aria-label="Small figure icon"></div>
<h2 class="abs section-title" style="left:220px;top:613px">Our Servces:</h2>

<article class="abs card" style="left:196px">
  <div class="thumb" role="img" aria-label="Group of business figures"></div>
  <h3>Managed<br>IT Services</h3>
  <p>Marlune is an IT outsourcing provider supplying small and medium sized businesses like yours with networking ..</p>
  <svg class="more" width="14" height="10" viewBox="0 0 14 10"><path d="M1 1l4 4-4 4M7 1l4 4-4 4" fill="none" stroke="#c41a1a" stroke-width="2.2"/></svg>
</article>
<article class="abs card" style="left:358px">
  <div class="thumb" role="img" aria-label="Storage server with connections"></div>
  <h3 style="top:14px;left:87px;width:70px">Storage and Virtualization</h3>
  <p>Marlune's Storage and Virtualization Services incorporate ongoing support, maintenance, operations ..</p>
  <svg class="more" width="14" height="10" viewBox="0 0 14 10"><path d="M1 1l4 4-4 4M7 1l4 4-4 4" fill="none" stroke="#c41a1a" stroke-width="2.2"/></svg>
</article>
<article class="abs card" style="left:521px">
  <div class="thumb" role="img" aria-label="Networked computers" style="background:linear-gradient(135deg,#e8f4fb,#6fb4e0)"></div>
  <h3 style="top:13px;left:92px">Networking</h3>
  <p>Marlune can help your small business keep your computer network under control. We are a complete network..</p>
  <svg class="more" width="14" height="10" viewBox="0 0 14 10"><path d="M1 1l4 4-4 4M7 1l4 4-4 4" fill="none" stroke="#c41a1a" stroke-width="2.2"/></svg>
</article>
<article class="abs card" style="left:684px">
  <div class="thumb" role="img" aria-label="Backup server rack" style="width:75px;background:linear-gradient(135deg,#bfc4ca,#3a3f45)"></div>
  <h3 style="left:93px;width:64px">Backup and Recovery</h3>
  <p>Your small business data is growing and data loss happens for many reasons. Hard drive crashes..</p>
  <svg class="more" width="14" height="10" viewBox="0 0 14 10"><path d="M1 1l4 4-4 4M7 1l4 4-4 4" fill="none" stroke="#c41a1a" stroke-width="2.2"/></svg>
</article>
<article class="abs card" style="left:845px">
  <div class="thumb" role="img" aria-label="Figure with repair tool" style="background:linear-gradient(135deg,#f4f4f4,#d96060)"></div>
  <h3 style="left:94px;top:12px;width:62px">Computer Repair Service</h3>
  <p>Malicious Code has become increasingly complex and infections involve more system elements ..</p>
  <svg class="more" width="14" height="10" viewBox="0 0 14 10"><path d="M1 1l4 4-4 4M7 1l4 4-4 4" fill="none" stroke="#c41a1a" stroke-width="2.2"/></svg>
</article>

<div class="abs section-icon" style="left:198px;top:784px;width:28px" role="img" aria-label="Two figures icon"></div>
<h2 class="abs section-title" style="left:229px;top:797px">We Work With:</h2>
<div class="abs partners"><ul>
  <li>Trevo</li><li>TL</li><li>Brax</li><li>VELK</li><li>Halvor</li><li>Quillsoft</li><li>Zentrix</li><li>Gatemoor</li>
</ul></div>

<footer class="abs footer"></footer>
<div class="abs footer-links">Home<span>|</span>Our Services<span>|</span>About us<span>|</span>Contact us</div>
<div class="abs copyright">Copyright © 2012 Marlune Solutions, All rights reserved</div>
<div class="abs footer-rule"></div>
</body>
</html>
```